Birchwell Landing - Multifamily Development

Birchwell Landing is a Luxury Multifamily Development project located in Orange, NJ. This project will be completed in three phases with the first phase about 75% complete. Each phase will have a different name as follows
CREST Birchwell Landing
RIDGE Birchwell Landing
ZENITHAL Birchwell Landing
We are going to install a banner on the side of the first building which will act as advertising for all buildings. We will eventually need advertising that will be in the windows as well as marketing materials . We want the marketing for this project to be similar for all three phases. At the moment, we are starting with this first simple banner. Attached is a rough idea of the look as well as our color palette. If you feel the color palette is a little too monochrome, feel free to propose an accent color. You can also visit our website to see more info on our company as well as the project. www.tolvarhq.com Finally, if you need AI files (ie. for the logo), we can send to you. Thanks..

```html
<!DOCTYPE html>
<html lang="en">
<head>
<meta charset="utf-8">
<title>Birchwell Landing – Now Leasing</title>
<link rel="stylesheet" href="https://fonts.googleapis.com/css2?family=Poppins:wght@300;400;500;600;700&family=Roboto+Condensed:wght@700&display=swap">
<style>
  :root {
    --navy: #3f5170;
    --slate: #8899b3;
    --ink: #3f5b86;
    --paper: #ffffff;
    --accent: #e39b3b;
  }
  * { margin: 0; padding: 0; box-sizing: border-box; }
  html, body { width: 1200px; height: 877px; overflow: hidden; background: var(--navy); }
  .banner { position: relative; width: 1200px; height: 877px; background: var(--navy); font-family: "Poppins", sans-serif; }
  .panel { position: absolute; background: var(--paper); }
  .panel--slate { background: var(--slate); }
  .panel--brand { left: 94px; top: 81px; width: 329px; height: 136px; display: flex; align-items: center; justify-content: center; }
  .panel--now { left: 435px; top: 81px; width: 328px; height: 136px; }
  .panel--leasing { left: 776px; top: 81px; width: 329px; height: 136px; }
  .panel--name { left: 94px; top: 230px; width: 329px; height: 566px; }
  .panel--contact { left: 435px; top: 230px; width: 328px; height: 566px; }
  .panel--units { left: 776px; top: 230px; width: 329px; height: 566px; }

  .brand-name { color: var(--paper); font-weight: 700; font-size: 60px; letter-spacing: 1px; line-height: 1; }
  .headline { position: absolute; left: 0; right: 0; top: 64px; text-align: center; color: var(--ink); font-weight: 400; font-size: 58px; line-height: 1; }

  .project-name {
    position: absolute; left: 258px; top: 504px; width: 440px; height: 132px;
    margin-left: -220px; margin-top: -66px; transform: rotate(-90deg);
    color: var(--ink); font-weight: 300; font-size: 64px; line-height: 64px; letter-spacing: 2px;
  }
  .project-name span { display: block; white-space: nowrap; }

  .contact { position: absolute; left: 472px; width: 247px; color: var(--paper); font-family: "Roboto Condensed", sans-serif; font-weight: 700; line-height: 1; white-space: nowrap; }
  .contact--project { top: 352px; font-size: 21px; }
  .contact--phone { top: 380px; font-size: 29px; }
  .contact--email { top: 418px; font-size: 22px; }
  .contact--web { top: 450px; font-size: 22px; letter-spacing: 4px; }
  .rule { position: absolute; height: 5px; background: var(--accent); }
  .rule--contact { left: 472px; top: 498px; width: 244px; }
  .tagline { position: absolute; left: 472px; color: var(--paper); font-weight: 600; line-height: 1; white-space: nowrap; }
  .tagline--top { top: 525px; font-size: 28px; letter-spacing: 8px; }
  .tagline--bottom { top: 554px; font-size: 30px; letter-spacing: 1.5px; }
  .lifestyle-art { position: absolute; left: 468px; top: 619px; width: 254px; height: 146px; background: linear-gradient(180deg, #9eacc2, #c8d1de); border-radius: 4px; }

  .rule--units-top { left: 824px; top: 352px; width: 225px; }
  .rule--units-bottom { left: 824px; top: 639px; width: 225px; }
  .units { position: absolute; left: 824px; color: var(--ink); line-height: 1; white-space: nowrap; }
  .units--studio { top: 383px; font-size: 55px; font-weight: 500; letter-spacing: 1px; }
  .units--count { top: 426px; font-size: 104px; font-weight: 500; }
  .units--bedroom { top: 525px; font-size: 46px; font-weight: 500; }
  .units--apartments { top: 575px; font-size: 36px; font-weight: 500; }
</style>
</head>
<body>
<main class="banner">
  <div class="panel panel--slate panel--brand"><span class="brand-name">TOLVAR</span></div>
  <div class="panel panel--now"><p class="headline">NOW</p></div>
  <div class="panel panel--leasing"><p class="headline">LEASING</p></div>

  <div class="panel panel--name"></div>
  <h1 class="project-name"><span>BIRCHWELL</span><span>LANDING</span></h1>

  <div class="panel panel--slate panel--contact"></div>
  <p class="contact contact--project">CREST BIRCHWELL LANDING</p>
  <p class="contact contact--phone">CALL: 973.555.0142</p>
  <p class="contact contact--email">RENTALS@TOLVARHQ.COM</p>
  <p class="contact contact--web">WWW.TOLVARHQ.COM</p>
  <div class="rule rule--contact"></div>
  <p class="tagline tagline--top">EXCEEEDING</p>
  <p class="tagline tagline--bottom">EXPECTATIONS</p>
  <div class="lifestyle-art" role="img" aria-label="White silhouettes of residents: a woman with bags, a father lifting a child, and a girl doing a cartwheel"></div>

  <div class="panel panel--units"></div>
  <div class="rule rule--units-top"></div>
  <p class="units units--studio">STUDIO,</p>
  <p class="units units--count">1&amp; 2</p>
  <p class="units units--bedroom">BEDROOM</p>
  <p class="units units--apartments">APARTMENTS</p>
  <div class="rule rule--units-bottom"></div>
</main>
</body>
</html>
```